Contemporary update for a market leader in foodservice distribution

KORVELT is a market leader in foodservice distribution nationwide.
We have recently adopted a new look and feel for our flagship foodservice rewards programme, and we're looking to have our business cards reflect our new aesthetic. Below is a link to our new rewards website to give you a general idea on the look we're after. https://korveltperks.com.au/

Industry/Entity Type

Distribution

Contact Information for Business Card

Must have space for contact name, position, company name and ABN, address, phone number and direct number, fax, email, and web address.

Font styles to use
Serif
Sans Serif

Requirements
Must have
• We'd like a landscape design, with our 'Tip of the Peak' logo incorporated on either the front or the back of the card. The overall design should be contemporary and professional.
Nice to have
• I have included both the full colour and white version of our company logo - our preference is to have the company logo one solid colour (white, or a shade of grey) although we're also open to designs including the full colour logo. If you are able to incorporate a small Facebook and LinkedIn logo, please do so.
Should not have
• Should not have an over-complicated design. No images of globes, or food.

```html
<!DOCTYPE html>
<html lang="en">
<head>
<meta charset="utf-8">
<title>KORVELT Business Card</title>
<link href="https://fonts.googleapis.com/css2?family=Raleway:wght@200;400&family=Open+Sans:wght@400&family=Great+Vibes&family=Montserrat:wght@800&display=swap" rel="stylesheet">
<style>
  :root {
    --frame: #2b2b2b;
    --paper: #f5f6f8;
    --sage: #d3e3d9;
    --ink: #2b2b2b;
    --muted: #7b7e82;
    --brand: #1f8f4a;
    --canvas: #f0f0f0;
  }
  html, body {
    margin: 0;
    padding: 0;
    overflow: hidden;
  }
  body {
    width: 1052px;
    height: 1200px;
    background: var(--canvas);
    position: relative;
    font-family: "Open Sans", sans-serif;
    color: var(--muted);
  }
  .card {
    position: absolute;
    left: 43px;
    width: 946px;
    box-sizing: border-box;
    border: 10px solid var(--frame);
  }
  .card-front { top: 28px; height: 556px; background: var(--paper); }
  .card-back { top: 611px; height: 553px; background: var(--sage); }

  .name-panel {
    position: absolute;
    left: 262px;
    top: -4px;
    width: 419px;
    height: 245px;
    box-sizing: border-box;
    border: 8px solid var(--frame);
    background: var(--sage);
    display: flex;
    align-items: center;
    justify-content: center;
    text-align: center;
  }
  .name {
    margin: 0;
    font-family: "Raleway", sans-serif;
    font-weight: 200;
    font-size: 56px;
    line-height: 1.15;
    letter-spacing: 2px;
    color: var(--ink);
  }
  .script {
    font-family: "Great Vibes", cursive;
    color: var(--ink);
  }
  .role {
    position: absolute;
    left: 0; right: 0;
    top: 258px;
    text-align: center;
    font-size: 30px;
  }
  .email {
    position: absolute;
    left: 0; right: 0;
    top: 296px;
    text-align: center;
    font-size: 21px;
  }
  .email .script, .contact .script { font-size: 27px; }

  .contact {
    position: absolute;
    font-size: 21px;
    line-height: 30px;
  }
  .contact-left { left: 36px; top: 436px; }
  .contact-right { left: 618px; top: 436px; }
  .contact .row { display: flex; }
  .contact .label { display: inline-block; width: 66px; }
  .contact-right .label { width: 77px; }

  .brand-mark {
    display: flex;
    align-items: center;
    gap: 10px;
    font-family: "Raleway", sans-serif;
    font-weight: 400;
    color: var(--ink);
  }
  .brand-dot {
    border-radius: 50%;
    background: var(--brand);
    flex: none;
  }
  .brand-front {
    position: absolute;
    left: 390px;
    top: 430px;
    font-size: 30px;
  }
  .brand-front .brand-dot { width: 26px; height: 26px; }
  .social {
    position: absolute;
    left: 460px;
    top: 488px;
    display: flex;
    gap: 10px;
  }
  .social span {
    width: 21px;
    height: 21px;
    background: var(--ink);
  }

  .brand-back {
    position: absolute;
    left: 27px;
    top: 38px;
    font-size: 48px;
  }
  .brand-back .brand-dot { width: 44px; height: 44px; }
  .website {
    position: absolute;
    right: 30px;
    top: 40px;
    font-size: 21px;
  }
  .website .script { font-size: 27px; }

  .award-panel {
    position: absolute;
    left: 262px;
    top: 297px;
    width: 419px;
    height: 246px;
    box-sizing: border-box;
    border: 8px solid var(--frame);
    border-bottom: none;
    background: var(--paper);
    display: flex;
    align-items: center;
    justify-content: center;
  }
  .award-mark {
    font-family: "Raleway", sans-serif;
    font-weight: 400;
    font-size: 38px;
    color: var(--ink);
  }
  .award-mark .brand-dot { width: 34px; height: 34px; }
</style>
</head>
<body>
  <section class="card card-front">
    <div class="name-panel">
      <h1 class="name">MARCUS<br>HALE</h1>
    </div>
    <div class="role script">Business Manager</div>
    <div class="email"><span class="script">Email</span>: info@korvelt.com</div>

    <div class="contact contact-left">
      <div class="row"><span class="label script">Phone:</span><span>+00 000 000 0000</span></div>
      <div class="row"><span class="label"></span><span>+00 000 000 0000</span></div>
      <div class="row"><span class="label script">Abn :</span><span>&nbsp;&nbsp;00 000 000 000</span></div>
    </div>

    <div class="brand-mark brand-front"><span class="brand-dot"></span>KORVELT</div>
    <div class="social" aria-label="Social media">
      <span></span><span></span>
    </div>

    <div class="contact contact-right">
      <div class="row"><span class="label script">Address:</span><span>4180 Calder Avenue</span></div>
      <div class="row"><span class="label"></span><span>Dunmore, PA 18512</span></div>
      <div class="row"><span class="label script">Fax:</span><span>(00) 0000 0000</span></div>
    </div>
  </section>

  <section class="card card-back">
    <div class="brand-mark brand-back"><span class="brand-dot"></span>KORVELT</div>
    <div class="website"><span class="script">Website</span> : www.korvelt.com</div>
    <div class="award-panel">
      <div class="brand-mark award-mark"><span class="brand-dot"></span>Tip of the Peak</div>
    </div>
  </section>
</body>
</html>
```